2016 QMB Tournament Trail Schedule

I need a flyer designed for our 2016 QMB Trail. We are a Texas based bass tournament trail. We are announcing $10K guaranteed for first at all 6 regular season events and $20K guaranteed for first at our 2 day fall championship. On the flyer we'd also like to show our schedule.

Jan 30 - Lake LBJ
Feb 27 - Canyon Lake
April 2 - Lake Travis
April 30 - Belton Lake
May 21 - Lake Buchanan
June 18 - Lake Waco

Fall Championship - TBD

Adult teams $200 entry includes big bass pot
Youth/adult teams $150 entry includes big bass pot

The flyer needs to be bass fishing related and we can provide pictures if you have ideas. We do not want it to look redneck'ish though. Our website is qmb1.net and would prefer a similar look. Lot's of black, red, and grey.

We have attached the QMB logo and we would also like Norvane and Dolkira logos incorporated. Norvane boats (which are are owned by Dolkira motors) is our title sponsor

Target Market(s)

Our anglers

Font styles to use
Other font styles liked:
• Something Cool

Colors
474747
ec1f27
000000
dbdbdb

Requirements
Must have
• Tournament dates and locations entry costs, payout guarantees
• QMB logo, Norvane Logo, Dolkira Logo
Nice to have
• go to www.qmb1.net to see our website, this should give you a feel for our style
• or qmbforum.net another site we operate

```html
<!DOCTYPE html>
<html lang="en">
<head>
<meta charset="utf-8">
<title>2016 QMB Tournament Trail Schedule</title>
<link href="https://fonts.googleapis.com/css2?family=Oswald:wght@400;500;700&display=swap" rel="stylesheet">
<style>
  :root {
    --red: #ec1f27;
    --dark-red: #b3141b;
    --black: #000000;
    --charcoal: #474747;
    --light: #dbdbdb;
    --white: #ffffff;
  }
  * { margin: 0; padding: 0; box-sizing: border-box; }
  html, body { width: 885px; height: 1200px; overflow: hidden; background: var(--light); }
  .flyer {
    position: relative; width: 885px; height: 1200px; overflow: hidden;
    background: var(--black); font-family: "Oswald", sans-serif; color: var(--white);
  }
  .top-band { position: absolute; left: 0; top: 0; width: 885px; height: 110px; background: var(--white); }
  .brand { position: absolute; left: 34px; top: 26px; display: flex; align-items: center; gap: 12px; }
  .brand-mark { width: 26px; height: 26px; background: var(--red); }
  .brand-name { font-size: 44px; font-weight: 700; color: var(--charcoal); letter-spacing: 2px; line-height: 1; }
  .hero-photo {
    position: absolute; left: 0; top: 110px; width: 400px; height: 520px;
    background: linear-gradient(160deg, #cfd8de 0%, #8a9aa6 45%, #3c4a55 100%);
  }
  .title-panel {
    position: absolute; left: 400px; top: 0; width: 485px; height: 630px;
    background: linear-gradient(180deg, var(--red) 0%, var(--dark-red) 100%);
    padding: 92px 34px 0 40px; text-align: center;
  }
  .title { font-weight: 700; font-size: 64px; line-height: 1.05; text-transform: uppercase; }
  .title .year-line { font-size: 72px; }
  .announcement {
    margin-top: 26px; font-weight: 500; font-size: 25px; line-height: 1.25;
    text-transform: uppercase; text-align: left;
  }
  .torn-edge { position: absolute; left: 0; top: 560px; width: 885px; height: 110px; }
  .schedule {
    position: absolute; left: 36px; top: 686px; width: 384px; height: 168px;
    background: var(--red); border: 2px solid var(--white); padding: 12px 16px;
  }
  .schedule-title {
    text-align: center; font-size: 24px; font-weight: 500; text-transform: uppercase;
    border-bottom: 1px solid var(--white); padding-bottom: 6px; margin-bottom: 12px;
  }
  .schedule-list {
    display: grid; grid-template-columns: 168px 180px; gap: 8px 0;
    list-style: none; font-size: 15px; white-space: nowrap;
  }
  .schedule-list li::before { content: "•"; margin-right: 6px; }
  .pin { position: absolute; top: 644px; width: 2px; height: 44px; background: var(--white); }
  .pin::before { content: ""; position: absolute; left: -5px; top: -10px; width: 12px; height: 12px; border-radius: 50%; background: var(--white); }
  .details { position: absolute; left: 470px; top: 700px; width: 390px; }
  .championship { font-size: 26px; font-weight: 500; text-transform: uppercase; margin-bottom: 20px; }
  .entry { font-size: 21px; line-height: 1.3; padding-left: 14px; margin-bottom: 16px; position: relative; }
  .entry::before { content: ""; position: absolute; left: 0; top: 4px; width: 3px; height: 48px; background: var(--red); }
  .angler-photo {
    position: absolute; left: 220px; top: 900px; width: 360px; height: 260px;
    background: radial-gradient(ellipse at 50% 40%, #6d6a55 0%, #3d3a2c 55%, #111 100%);
  }
  .sponsors { position: absolute; left: 40px; top: 1010px; display: flex; flex-direction: column; gap: 22px; }
  .sponsor { font-size: 26px; font-weight: 700; color: var(--white); text-transform: uppercase; letter-spacing: 2px; }
  .web-band {
    position: absolute; left: 610px; top: 1080px; width: 275px; height: 56px;
    background: var(--red); display: flex; align-items: center; justify-content: center;
    font-size: 27px; font-weight: 500; letter-spacing: 1px;
  }
  .base-strip { position: absolute; left: 0; bottom: 0; width: 885px; height: 40px; background: var(--charcoal); }
</style>
</head>
<body>
<main class="flyer">
  <div class="top-band"></div>
  <div class="brand">
    <span class="brand-mark"></span>
    <span class="brand-name">QMB</span>
  </div>

  <div class="hero-photo" role="img" aria-label="Angler fighting a bass with a bent rod from the deck of a boat on open water"></div>

  <section class="title-panel">
    <h1 class="title"><span class="year-line">2016 QMB</span><br>Tournament<br>Trail Schedule</h1>
    <p class="announcement">We are announcing $10K guaranteed for first at all 6 regular season events and $20K guaranteed at our 2 day fall championship</p>
  </section>

  <svg class="torn-edge" viewBox="0 0 885 110" preserveAspectRatio="none" aria-hidden="true">
    <polygon fill="#000000" points="0,70 40,58 70,72 110,50 150,66 190,44 230,60 270,38 310,55 350,30 390,48 430,26 470,42 510,20 550,38 590,16 630,34 670,12 710,30 750,10 790,26 830,6 885,20 885,110 0,110"/>
    <polyline fill="none" stroke="#dbdbdb" stroke-width="3" points="0,70 40,58 70,72 110,50 150,66 190,44 230,60 270,38 310,55 350,30 390,48 430,26 470,42 510,20 550,38 590,16 630,34 670,12 710,30 750,10 790,26 830,6 885,20"/>
  </svg>

  <span class="pin" style="left:110px"></span>
  <span class="pin" style="left:340px"></span>
  <section class="schedule">
    <h2 class="schedule-title">Our Schedule</h2>
    <ul class="schedule-list">
      <li>Jan 30 - Lake LBJ</li>
      <li>April 30 - Belton Lake</li>
      <li>Feb 27 - Canyon Lake</li>
      <li>May 21 - Lake Buchanan</li>
      <li>April 2 - Lake Travis</li>
      <li>June 18 - Lake Waco</li>
    </ul>
  </section>

  <section class="details">
    <h2 class="championship">Fall Championship - TBD</h2>
    <p class="entry">Adult teams $200 entry includes<br>big bass pot</p>
    <p class="entry">Youth/adult teams $150 entry<br>includes big bass pot</p>
  </section>

  <div class="angler-photo" role="img" aria-label="Angler kneeling and holding up a large bass"></div>

  <div class="sponsors">
    <span class="sponsor">Norvane</span>
    <span class="sponsor">Dolkira</span>
  </div>

  <div class="web-band">www.qmb1.net</div>
  <div class="base-strip"></div>
</main>
</body>
</html>
```